vault key finders.com

we are a new company that offer people that have lost there bit coin transaction a recovery and retrieval service
We are looking for a website that will allow you to fill in your details

name
email
bitcoins or other crypto lost and date of transaction

and then an auto reply to them from a given email to verify there email

I am looking for an easy for the client to leave there interest and has a security look around it and looks familiar to the user.

https://purserestore.example/?ref=Xq7LmT2vNp9RsK4wYb8ZcD1fGh6JkM3nQe5UtV0aBy

https://pursemendingaid.example

https://www.zennoro.example/faq-items/restoring-your-token-purse/

Target Market(s)

early investors into crypto

Industry/Entity Type

It Company

Logo Text

VAULTKEY FINDERS/LOCATORS

Coding

Coded - Design and coding required

Number of Pages Required

3 page

Requirements
Must have
• be able to :
• complete
• Name,
• Email
• transaction date of exchange and how much they invested

```html
<!DOCTYPE html>
<html lang="en">
<head>
<meta charset="utf-8">
<title>Vault Key Finders</title>
<link href="https://fonts.googleapis.com/css2?family=Roboto:wght@300;400;500;700&display=swap" rel="stylesheet">
<style>
:root{
  --blue:#1e9bd7;
  --orange:#f7941d;
  --ink:#4a4f55;
  --muted:#6b7178;
  --page:#f7f9fc;
  --band:#e6e9ed;
  --line:#e2e6ea;
  --white:#ffffff;
}
*{margin:0;padding:0;box-sizing:border-box}
html,body{width:816px;height:1200px;overflow:hidden;background:var(--page);font-family:'Roboto',sans-serif;color:var(--ink)}
.page{position:relative;width:816px;height:1200px}
.hero{position:absolute;left:0;top:0;width:816px;height:411px;background:linear-gradient(160deg,#8b8a6a 0%,#5d6a63 30%,#2f4a63 60%,#23364a 100%)}
.hero-photo{position:absolute;inset:0}
.site-header{position:absolute;top:0;left:0;width:816px;height:42px}
.brand{position:absolute;left:117px;top:12px;color:var(--white);font-weight:500;font-size:15px}
.nav{position:absolute;right:146px;top:16px;display:flex;gap:14px;align-items:center;font-size:7.5px;font-weight:400;color:var(--white)}
.nav .signup{background:var(--orange);padding:3px 9px;border-radius:1px}
.hero h1{position:absolute;top:185px;width:100%;text-align:center;color:var(--white);font-size:31px;font-weight:500}
.hero .lead{position:absolute;top:224px;width:100%;text-align:center;color:#eef2f5;font-size:9.5px;font-weight:300}
.lead-form{position:absolute;top:253px;left:187px;width:441px;display:flex;flex-wrap:wrap;gap:6px}
.lead-form .field{height:31px;background:var(--white);border-radius:2px;font-size:10px;font-weight:400;color:#666;padding:10px 10px;white-space:nowrap}
.lead-form .wide{width:174px}
.lead-form .third{width:143px}
.lead-form .btn{width:81px;height:31px;background:var(--orange);color:var(--white);font-size:8.5px;font-weight:500;display:flex;align-items:center;justify-content:center;border-radius:2px}
.features-title{position:absolute;top:450px;width:100%;text-align:center;font-size:22px;font-weight:400;color:#5a5f66}
.feature{position:absolute;top:498px;width:155px;height:165px;background:var(--white);box-shadow:0 1px 3px rgba(0,0,0,.06);text-align:center}
.feature .icon{width:63px;height:63px;border-radius:50%;background:#eef1f4;margin:25px auto 0;display:flex;align-items:center;justify-content:center}
.feature h3{margin-top:9px;font-size:11px;font-weight:400;color:var(--blue)}
.feature p{margin-top:6px;font-size:7.5px;font-weight:300;line-height:11px;color:var(--muted)}
.divider{position:absolute;top:698px;left:118px;width:580px;height:1px;background:var(--line)}
.devices{position:absolute;left:117px;top:728px;width:268px;height:214px;background:linear-gradient(180deg,#2b4a7e 0%,#c9cdd2 70%,#e9ebee 100%);border-radius:6px}
.steps{position:absolute;left:411px;top:728px;width:290px}
.steps h2{font-size:21px;font-weight:400;color:#5a5f66}
.steps ol{list-style:none;margin-top:9px}
.steps li{position:relative;padding-left:12px;font-size:9.5px;font-weight:300;line-height:11px;color:var(--muted);margin-bottom:13px}
.steps li::before{content:"";position:absolute;left:0;top:2px;width:7px;height:7px;border-radius:50%;background:var(--orange)}
.partners{position:absolute;top:1011px;left:0;width:816px;height:50px;background:var(--band);display:flex;justify-content:space-between;align-items:center;padding:0 134px 0 124px}
.partner{display:flex;align-items:center;gap:5px;font-size:14px;font-weight:500;color:#6a6f75}
.partner .dot{width:11px;height:11px;background:#6a6f75;border-radius:2px}
.footer-cols{position:absolute;top:1082px;left:117px;display:flex}
.col h4{font-size:8px;font-weight:400;color:#454a50;margin-bottom:8px}
.col a{display:block;font-size:7px;color:var(--blue);text-decoration:none;line-height:12px}
.social{display:flex;gap:6px;margin-bottom:8px}
.social span{width:24px;height:24px;border-radius:50%;background:var(--white);border:1px solid var(--line);font-size:5.5px;display:flex;align-items:center;justify-content:center;color:var(--blue)}
.cards{display:flex;gap:4px}
.cards span{width:24px;height:14px;background:#d8dde3;font-size:5px;color:#454a50;display:flex;align-items:center;justify-content:center}
.footer-line{position:absolute;top:1176px;left:118px;width:580px;height:1px;background:var(--line)}
.copyright{position:absolute;top:1184px;width:100%;text-align:center;font-size:7px;color:var(--muted)}
</style>
</head>
<body>
<div class="page">
  <section class="hero">
    <div class="hero-photo" role="img" aria-label="Photo of a young man in a beanie and glasses looking at his phone outdoors"></div>
    <header class="site-header">
      <div class="brand">Vault Key Finders</div>
      <nav class="nav"><span>Accept Bitcoin</span><span>Wallet</span><span>Card</span><span>Docs</span><span>Log In</span><span class="signup">Sign Up</span></nav>
    </header>
    <h1>Get Your Bitcoin Wallet Back</h1>
    <p class="lead">Lost your Bitcoin wallet? We can help. No charge unless we succeed.</p>
    <div class="lead-form">
      <div class="field wide">Name</div>
      <div class="field wide">Email</div>
      <div class="btn">Get Started</div>
      <div class="field third">Crypto lost (e.g. BTC)</div>
      <div class="field third">Transaction date</div>
      <div class="field third">Amount invested</div>
    </div>
  </section>

  <h2 class="features-title">Recovering your bitcoin wallet</h2>
  <div class="feature" style="left:153px">
    <div class="icon"><svg width="38" height="38" viewBox="0 0 38 38" fill="none" stroke="#1e9bd7" stroke-width="2.5"><circle cx="19" cy="19" r="16"/><circle cx="19" cy="19" r="9"/></svg></div>
    <h3>Accept bitcoin</h3><p>Accept bitcoin payments<br>for your business.</p>
  </div>
  <div class="feature" style="left:331px">
    <div class="icon"><svg width="44" height="34" viewBox="0 0 44 34" fill="none" stroke="#1e9bd7" stroke-width="2.5"><rect x="4" y="3" width="30" height="22" rx="2"/><path d="M1 29h36"/><path d="M11 10h6M11 17h6M21 11h8M21 17h8"/><rect x="31" y="16" width="11" height="10" fill="#1e9bd7"/><path d="M33 16v-3a3.5 3.5 0 0 1 7 0v3"/></svg></div>
    <h3>Securely store bitcoin</h3><p>Get a bitcoin wallet and<br>start using bitcoin.</p>
  </div>
  <div class="feature" style="left:508px">
    <div class="icon"><svg width="36" height="38" viewBox="0 0 36 38" fill="none" stroke="#1e9bd7" stroke-width="2.5"><rect x="2" y="3" width="32" height="10" rx="2"/><rect x="10" y="8" width="16" height="28" fill="#1e9bd7"/></svg></div>
    <h3>Spend anywhere</h3><p>Turn bitcoin into dollars<br>and spend anywhere.</p>
  </div>

  <div class="divider"></div>

  <div class="devices" role="img" aria-label="Illustration of a desktop screen, phone and smartwatch showing a wallet dashboard"></div>
  <section class="steps">
    <h2>How to do it</h2>
    <ol>
      <li>Go to this page, enter your wallet passphrase and copy your wallet passcode</li>
      <li>Go to the Keystep Recovery tool. You can either use the online version or for ever more security, you can run it offline.</li>
      <li>First form field: Enter the wallet passcode you got from the popup on the Zennoro page</li>
      <li>Second, Third and Forth form fields: Copy and paste the data next to the QR codes into the form for the top three qr codes</li>
      <li>Fith field: Enter your new bitcoin address</li>
    </ol>
  </section>

  <div class="partners">
    <div class="partner"><span class="dot"></span>Armorvault</div>
    <div class="partner">Coinlane</div>
    <div class="partner"><span class="dot"></span>Keystep</div>
    <div class="partner"><span class="dot"></span>Morphswap</div>
    <div class="partner"><span class="dot"></span>tokenhaus</div>
  </div>

  <footer>
    <div class="footer-cols">
      <div class="col" style="width:98px"><h4>Businesses</h4><a>Accept Bitcoin</a><a>Integrations</a><a>Documentation</a><a>Pricing</a><a>Payouts</a></div>
      <div class="col" style="width:100px"><h4>Individuals</h4><a>Pay with Bitcoin</a><a>Pursely Card</a><a>Pursely Card FAQs</a><a>Pursely Wallet</a></div>
      <div class="col" style="width:89px"><h4>Developers</h4><a>Developer Docs</a><a>Corekit</a><a>Insight</a><a>Open Source</a></div>
      <div class="col" style="width:83px"><h4>Company</h4><a>About</a><a>Team</a><a>Press</a><a>Terms of Use</a></div>
      <div class="col"><h4>Follow us</h4>
        <div class="social"><span>Loop</span><span>Chirp</span><span>Gleam</span><span>Linka</span></div>
        <div class="cards"><span>Cardora</span><span>Tallypay</span><span>Orbix</span><span>Dexa</span></div>
      </div>
    </div>
    <div class="footer-line"></div>
    <p class="copyright">2018 all rights reserved.</p>
  </footer>
</div>
</body>
</html>
```